Gin Bottle label design

A label for three Gins, 1 Apple flavoured, 1 Bilberry flavoured and one London Dry Gin. All need to incorporate the business logo that i've attached along with the bottle we intend to use. The gin is 40% and will be in a 70cl bottle

```html
<!DOCTYPE html>
<html lang="en">
<head>
<meta charset="utf-8">
<title>London Dry Gin – Label</title>
<link rel="stylesheet" href="https://fonts.googleapis.com/css2?family=Cinzel:wght@500&family=Oswald:wght@600&family=Great+Vibes&display=swap">
<style>
  :root {
    --backdrop-light: #eceef1;
    --backdrop-dark: #9da1a8;
    --label-black: #0b0b0b;
    --label-sheen: #343434;
    --botanical-grey: #5a5a5a;
    --gold-light: #f1d39a;
    --gold-mid: #c9995b;
    --gold-deep: #7a5a2e;
    --cream: #fbeed0;
  }
  * { box-sizing: border-box; margin: 0; padding: 0; }
  html, body { width: 1200px; height: 801px; overflow: hidden; }
  body {
    background: linear-gradient(120deg, var(--backdrop-dark) 0%, var(--backdrop-light) 70%, #ffffff 100%);
    position: relative;
  }
  .label {
    position: absolute;
    left: 250px; top: 70px;
    width: 700px; height: 660px;
    background: radial-gradient(ellipse 60% 55% at 55% 55%, var(--label-sheen) 0%, var(--label-black) 75%);
    box-shadow: 0 18px 40px rgba(0,0,0,.35);
    overflow: hidden;
  }
  .botanicals {
    position: absolute; left: 0; top: 0; width: 700px; height: 400px;
  }
  .brand {
    position: absolute; left: 0; right: 0; top: 120px;
    display: flex; align-items: center; justify-content: center; gap: 22px;
  }
  .brand-ring {
    width: 150px; height: 150px; border-radius: 50%;
    border: 4px solid var(--gold-mid);
    background: var(--label-black);
    flex: none;
  }
  .brand-name {
    font-family: "Cinzel", serif; font-weight: 500;
    font-size: 36px; letter-spacing: 3px; line-height: 1.2;
    color: var(--gold-mid);
  }
  .product-name {
    position: absolute; left: 0; right: 0; top: 360px;
    text-align: center;
    font-family: "Oswald", sans-serif; font-weight: 600;
    font-size: 96px; letter-spacing: 2px; line-height: 1;
    background: linear-gradient(90deg, var(--gold-light), var(--gold-mid) 45%, var(--gold-deep) 70%, var(--gold-mid));
    -webkit-background-clip: text; background-clip: text;
    color: transparent;
  }
  .gold-band {
    position: absolute; left: 20px; right: 20px; top: 510px; height: 110px;
  }
  .gold-band svg { position: absolute; inset: 0; width: 100%; height: 100%; }
  .band-text {
    position: absolute; inset: 0;
    display: flex; align-items: center; justify-content: space-between;
    padding: 0 34px;
  }
  .band-detail {
    font-family: "Oswald", sans-serif; font-weight: 600;
    font-size: 20px; letter-spacing: 1px; color: var(--label-black);
  }
  .band-tagline {
    font-family: "Great Vibes", cursive;
    font-size: 50px; color: var(--cream);
    text-shadow: 0 1px 2px rgba(0,0,0,.5);
  }
</style>
</head>
<body>
  <main class="label">
    <svg class="botanicals" viewBox="0 0 700 400" role="img" aria-label="Grey line illustration of gin botanicals: juniper sprigs, berries, blossoms and herbs">
      <defs>
        <radialGradient id="botanical-tone" cx="35%" cy="35%" r="75%">
          <stop offset="0%" stop-color="var(--botanical-grey)" stop-opacity="0.55"/>
          <stop offset="60%" stop-color="var(--botanical-grey)" stop-opacity="0.3"/>
          <stop offset="100%" stop-color="var(--botanical-grey)" stop-opacity="0"/>
        </radialGradient>
      </defs>
      <rect width="700" height="400" fill="url(#botanical-tone)"/>
    </svg>

    <div class="brand">
      <span class="brand-ring"></span>
      <span class="brand-name">THE OLIVE<br>TABLE</span>
    </div>

    <h1 class="product-name">LONDON DRY GIN</h1>

    <div class="gold-band">
      <svg viewBox="0 0 660 110" preserveAspectRatio="none" role="img" aria-label="Gold band with fine lattice pattern">
        <defs>
          <linearGradient id="band-gold" x1="0" y1="0" x2="1" y2="0">
            <stop offset="0%" stop-color="var(--gold-deep)"/>
            <stop offset="30%" stop-color="var(--gold-light)"/>
            <stop offset="60%" stop-color="var(--gold-mid)"/>
            <stop offset="100%" stop-color="var(--gold-deep)"/>
          </linearGradient>
        </defs>
        <rect width="660" height="110" fill="url(#band-gold)"/>
        <rect x="6" y="6" width="648" height="98" fill="none" stroke="var(--label-black)" stroke-opacity=".5" stroke-width="1.5"/>
      </svg>
      <div class="band-text">
        <span class="band-detail">70CL</span>
        <span class="band-tagline">Handcrafted</span>
        <span class="band-detail">40% ALC VOL</span>
      </div>
    </div>
  </main>
</body>
</html>
```